Clean Technology Flyer

This is a brand new award winning industrial cleaning technology. Please see our website.

Preferable a single page brochure or a fold-able brochure.

Target Market(s)

Meridian 300 executives, Senior Manages, Plant Managers.

Industry/Entity Type

Industrial

Colors

Designer to choose colors to be used in the design.

Requirements
Must have
• Website
• Name
• Logo
• Proper Branding
Nice to have
• Clean, Modern, Elegant. I am looking for a design such as Lumio might have.
• I like the font: Garamond.
Should not have
• I want less but more important information then I have on the current brochure attached to this.

```html
<!DOCTYPE html>
<html lang="en">
<head>
<meta charset="utf-8">
<title>FrostPulse Ice Blast Brochure</title>
<link rel="stylesheet" href="https://fonts.googleapis.com/css2?family=EB+Garamond:wght@400;600;700&family=Open+Sans:wght@400&display=swap">
<style>
  :root {
    --backdrop: #e4e4e4;
    --paper: #f4f5f8;
    --paper-shade: #e4e7ec;
    --brand-blue: #3f77ad;
    --title-blue: #4a7fb5;
    --ink: #2b2b2b;
    --ink-soft: #444;
    --snow: #c9cfd6;
    --snow-dark: #8e969e;
    --steel: #9aa3ad;
    --hose: #3e6fb0;
  }
  * { box-sizing: border-box; margin: 0; padding: 0; }
  html, body { width: 1200px; height: 789px; overflow: hidden; }
  body { background: var(--backdrop); position: relative; font-family: "EB Garamond", Garamond, serif; color: var(--ink); }

  .spread { position: absolute; left: 100px; top: 50px; width: 1000px; height: 690px; display: flex; box-shadow: 0 6px 24px rgba(0,0,0,.18); }
  .page { position: relative; width: 500px; height: 690px; background: var(--paper); overflow: hidden; }
  .page--left { background: linear-gradient(90deg, var(--paper) 88%, var(--paper-shade)); }
  .page--right { background: linear-gradient(90deg, var(--paper-shade), var(--paper) 12%); }

  .page-title { color: var(--title-blue); font-weight: 600; font-size: 25px; line-height: 1.15; }
  .bullets { list-style: none; font-size: 14.5px; line-height: 19px; color: var(--ink-soft); }
  .bullets li { position: relative; padding-left: 24px; }
  .bullets li::before { content: ""; position: absolute; left: 2px; top: 6px; border-left: 8px solid var(--ink); border-top: 4px solid transparent; border-bottom: 4px solid transparent; }
  .bullets .sub { padding-left: 48px; }
  .bullets .sub::before { left: 26px; }

  /* left page */
  .performance-title { position: absolute; left: 40px; top: 34px; }
  .spec-list { position: absolute; left: 40px; top: 84px; width: 300px; }
  .product-part { position: absolute; }
  .part-gun { left: 388px; top: 84px; width: 62px; height: 74px; border-radius: 12px 28px 8px 8px; background: linear-gradient(160deg, #d4d8de, var(--steel)); }
  .part-hose { left: 365px; top: 178px; width: 100px; height: 62px; border-radius: 50%; border: 11px solid var(--hose); }
  .part-wand { left: 350px; top: 258px; width: 115px; height: 16px; border-radius: 4px; background: linear-gradient(90deg, #6f9ad0, var(--hose)); }
  .part-case { left: 345px; top: 290px; width: 125px; height: 38px; border-radius: 6px; background: linear-gradient(180deg, #b8bec6, #7d858e); }

  .site-frame { position: absolute; left: 0; top: 410px; width: 310px; height: 280px; overflow: hidden; }
  .site-ring { position: absolute; left: -140px; top: 0; width: 440px; height: 440px; border-radius: 50%; background: var(--brand-blue); }
  .site-photo { position: absolute; left: -168px; top: -6px; width: 440px; height: 440px; border-radius: 50%; background: linear-gradient(180deg, #dfe3e8 0%, var(--snow) 40%, var(--snow-dark) 60%, #b8bfc6 100%); }
  .intro-copy { position: absolute; left: 318px; top: 488px; width: 160px; font-family: "Open Sans", Arial, sans-serif; font-size: 12px; line-height: 15px; text-align: justify; color: var(--ink); }

  /* right page */
  .promise-title { position: absolute; left: 40px; top: 40px; }
  .applications-title { position: absolute; left: 40px; top: 112px; font-size: 18px; font-weight: 700; color: #111; }
  .applications { position: absolute; top: 140px; }
  .applications--a { left: 40px; }
  .applications--b { left: 270px; top: 162px; }

  .band { position: absolute; left: 0; bottom: 0; width: 500px; height: 280px; }
  .app-photo { position: absolute; border-radius: 50%; border: 4px solid var(--brand-blue); }
  .photo-boat { left: 200px; top: 470px; width: 380px; height: 380px; border: none; background: linear-gradient(180deg, #c7d3df 0%, #f2f4f6 40%, #dde3e9 70%, #8c96a0 100%); }
  .photo-aircraft { left: 120px; top: 350px; width: 170px; height: 170px; background: linear-gradient(180deg, #9fb0c2, #e7ebef 50%, #6d7782); }
  .photo-worker { left: 32px; top: 360px; width: 118px; height: 118px; background: linear-gradient(160deg, #8a6b4a, #c9b89c 50%, #5d4b39); }
  .photo-machine { left: 30px; top: 472px; width: 156px; height: 156px; background: linear-gradient(160deg, #6f7a85, #d88a22 45%, #343a40); }
</style>
</head>
<body>
  <main class="spread">
    <section class="page page--left">
      <h2 class="page-title performance-title">Uncompromised Performance</h2>
      <ul class="bullets spec-list">
        <li>Simple operational controls</li>
        <li>Non-pressurized 90lb hopper</li>
        <li>110 V electrical plug</li>
        <li>Weight: 400 lbs</li>
        <li>Compact: 40"x26"x45"(LxWxH)</li>
        <li>Operating Pressure:</li>
        <li class="sub">80 PSI –150 PSI</li>
        <li class="sub">180 CFM –425 CFM</li>
        <li>PSI gauges measuring pressure in and out</li>
        <li>Variable feed rate: 0 –5 lbs per minute</li>
        <li>Anodized exterior panels</li>
        <li>Stainless steel option available</li>
        <li>36 month or 2000 hr warranty</li>
        <li>Lower levels of airborne contaminates</li>
        <li>Superior internal ice crusher</li>
        <li>Finely tuned to increase life cycle and efficiency.</li>
      </ul>

      <div class="product-part part-gun" role="img" aria-label="Blast gun"></div>
      <div class="product-part part-hose" role="img" aria-label="Coiled blue blast hose"></div>
      <div class="product-part part-wand" role="img" aria-label="Blast nozzle"></div>
      <div class="product-part part-case" role="img" aria-label="Hard carry case"></div>

      <div class="site-frame">
        <div class="site-ring"></div>
        <div class="site-photo" role="img" aria-label="Snowy job site with traffic cones"></div>
      </div>
      <p class="intro-copy">FrostPulse is the most efficient and environmentally friendly blasting unit in the industry. The design basis focused on simplicity which translates through to the exterior, operational controls, and internal workings of the unit.</p>
    </section>

    <section class="page page--right">
      <h2 class="page-title promise-title">Zero Airborne Contaminates.<br>Zero Compromises.</h2>
      <h3 class="applications-title">Ice Blast Applications</h3>
      <ul class="bullets applications applications--a">
        <li>Aerospace</li>
        <li>Automotive</li>
        <li>Building Restoration</li>
        <li>Building Remediation</li>
        <li>Engineered Wood</li>
        <li>Food and Beverage</li>
        <li>Foundry</li>
        <li>General Maintenance</li>
        <li>Locomotive</li>
        <li>Marine</li>
      </ul>
      <ul class="bullets applications applications--b">
        <li>Municipality</li>
        <li>Nuclear</li>
        <li>Packaging</li>
        <li>Petro Chemical</li>
        <li>Plastics &amp; Injection Molds</li>
        <li>Power Generation</li>
        <li>Printing</li>
        <li>Pulp and Paper</li>
        <li>Rubber</li>
      </ul>

      <svg class="band" viewBox="0 0 500 280" aria-hidden="true">
        <path d="M0 160 C120 60 300 50 500 110 L500 280 L0 280 Z" fill="var(--brand-blue)"/>
      </svg>
      <div class="app-photo photo-boat" role="img" aria-label="White motor yacht on dry dock"></div>
      <div class="app-photo photo-aircraft" role="img" aria-label="Passenger jet in maintenance hangar"></div>
      <div class="app-photo photo-worker" role="img" aria-label="Technician ice blasting equipment"></div>
      <div class="app-photo photo-machine" role="img" aria-label="Industrial printing machinery"></div>
    </section>
  </main>
</body>
</html>
```